Business Cards and others
Business cards, stationery, Powerpoint template and E-mail Header and Footer
Professional
Darian Lutrell
CEO
4827 Thornwick Ln
Harlow Creek OR 97512
darian@velmorix.com
www.velmorix.com

```html
<!DOCTYPE html>
<html lang="en">
<head>
<meta charset="utf-8">
<title>Velmorix Business Card</title>
<link href="https://fonts.googleapis.com/css2?family=Open+Sans:wght@400;600;700&display=swap" rel="stylesheet">
<style>
  :root {
    --bg: #e9ecee;
    --card: #ffffff;
    --brand: #1f9bd1;
    --band: #1d8fb3;
    --text: #4a4f55;
    --muted: #7b8188;
    --rule: #d4d8dc;
    --shadow: rgba(0,0,0,0.14);
  }
  html, body {
    margin: 0;
    width: 1200px;
    height: 629px;
    overflow: hidden;
    background: var(--bg);
    font-family: "Open Sans", Arial, sans-serif;
  }
  .stage {
    width: 1200px;
    height: 629px;
    display: flex;
    align-items: center;
    justify-content: center;
    gap: 60px;
  }
  .card {
    position: relative;
    width: 525px;
    height: 300px;
    background: var(--card);
    box-shadow: 0 6px 18px var(--shadow);
    overflow: hidden;
  }
  .brand {
    display: flex;
    align-items: center;
    gap: 12px;
  }
  .brand-dot {
    border-radius: 50%;
    background: var(--brand);
  }
  .brand-name {
    color: var(--brand);
    font-weight: 700;
    letter-spacing: -0.5px;
    white-space: nowrap;
  }
  .card-front { display: flex; align-items: center; justify-content: center; }
  .card-front .brand-dot { width: 62px; height: 62px; }
  .card-front .brand-name { font-size: 50px; }
  .card-back .brand {
    position: absolute;
    left: 40px;
    top: 42px;
    gap: 9px;
  }
  .card-back .brand-dot { width: 40px; height: 40px; }
  .card-back .brand-name { font-size: 32px; }
  .holder {
    position: absolute;
    left: 40px;
    top: 130px;
    width: 210px;
  }
  .holder-name {
    margin: 0;
    color: var(--brand);
    font-size: 15px;
    font-weight: 600;
  }
  .holder-role {
    margin: 2px 0 22px;
    color: var(--muted);
    font-size: 11px;
  }
  .holder-address {
    margin: 0;
    color: var(--text);
    font-size: 11px;
    line-height: 1.55;
    font-style: normal;
    white-space: nowrap;
  }
  .divider {
    position: absolute;
    left: 258px;
    top: 40px;
    width: 1px;
    height: 185px;
    background: var(--rule);
  }
  .contacts {
    position: absolute;
    left: 278px;
    top: 44px;
    margin: 0;
    padding: 0;
    list-style: none;
  }
  .contacts li {
    display: flex;
    align-items: center;
    gap: 9px;
    height: 25px;
    color: var(--text);
    font-size: 11.5px;
    white-space: nowrap;
  }
  .contacts svg { width: 16px; height: 16px; flex: none; }
  .band {
    position: absolute;
    left: 0;
    bottom: 0;
    width: 100%;
    height: 46px;
    background: var(--band);
    display: flex;
    align-items: center;
    justify-content: center;
    color: #ffffff;
    font-size: 11px;
    letter-spacing: 4px;
  }
</style>
</head>
<body>
<main class="stage">
  <section class="card card-front" aria-label="Card front">
    <div class="brand">
      <span class="brand-dot"></span>
      <span class="brand-name">Velmorix</span>
    </div>
  </section>

  <section class="card card-back" aria-label="Card back">
    <div class="brand">
      <span class="brand-dot"></span>
      <span class="brand-name">Velmorix</span>
    </div>

    <div class="holder">
      <p class="holder-name">Darian Lutrell</p>
      <p class="holder-role">CEO</p>
      <address class="holder-address">4827 Thornwick Ln<br>Harlow Creek OR 97512</address>
    </div>

    <div class="divider"></div>

    <ul class="contacts">
      <li>
        <svg viewBox="0 0 16 16"><circle cx="8" cy="8" r="8" fill="var(--brand)"/><path d="M5.2 4.2l1.6 0 .6 2-1 .8c.5 1.1 1.3 1.9 2.4 2.4l.8-1 2 .6v1.6c-3.6.3-6.7-2.8-6.4-6.4z" fill="#fff"/></svg>
        410-555-0182
      </li>
      <li>
        <svg viewBox="0 0 16 16"><circle cx="8" cy="8" r="8" fill="var(--brand)"/><rect x="5.6" y="3.5" width="4.8" height="9" rx="0.8" fill="#fff"/><rect x="6.4" y="4.6" width="3.2" height="5.6" fill="var(--brand)"/></svg>
        443-555-0147
      </li>
      <li>
        <svg viewBox="0 0 16 16"><circle cx="8" cy="8" r="8" fill="var(--brand)"/><circle cx="8" cy="8" r="3" fill="#fff"/></svg>
        lutrell1867
      </li>
      <li>
        <svg viewBox="0 0 16 16"><circle cx="8" cy="8" r="8" fill="var(--brand)"/><rect x="4" y="5.2" width="8" height="5.6" fill="#fff"/><path d="M4 5.2l4 3 4-3" fill="none" stroke="var(--brand)" stroke-width="0.9"/></svg>
        darian@velmorix.com
      </li>
      <li>
        <svg viewBox="0 0 16 16"><circle cx="8" cy="8" r="8" fill="var(--brand)"/><circle cx="8" cy="8" r="4" fill="none" stroke="#fff" stroke-width="1"/><path d="M4 8h8M8 4c-1.6 2.2-1.6 5.8 0 8M8 4c1.6 2.2 1.6 5.8 0 8" fill="none" stroke="#fff" stroke-width="0.8"/></svg>
        www.velmorix.com
      </li>
    </ul>

    <div class="band">www.velmorix.com</div>
  </section>
</main>
</body>
</html>
```